Veterinary Clinic Letterhead - Ridgeview Veterinary Surgery

We need a letterhead design for an established Veterinary Clinic in Mareeba called Ridgeview Veterinary Surgery. We are a moderate sized mixed animal veterinary clinic offering a wide variety of veterinary services. The design should use the same colour pattern as those in the logos supplied. The design should also include our address (48 Tulloch Road, Kelvale, Westmoor, 4902), phone number (07 4158 6734), email (admin@ridgeviewvets.com.au), website (www.ridgeviewvets.com.au) and our opening hours (8am to 5pm Monday to Friday and 8am to 12pm Saturday).
Target Market(s)
Pet owners
Industry/Entity Type
Veterinary
Requirements
Must have
- The logo or modification of it, business address, opening hours, website, phone number and email address

```html
<!DOCTYPE html>
<html lang="en">
<head>
<meta charset="utf-8">
<title>Ridgeview Veterinary Surgery – Letterhead</title>
<link rel="stylesheet" href="https://fonts.googleapis.com/css2?family=Open+Sans:wght@400;600&family=Lato:wght@400;700&display=swap">
<style>
  :root {
    --navy: #0d2a52;
    --ink: #4a4a4a;
    --paper: #ffffff;
    --backdrop: #e4e4e4;
  }
  * { box-sizing: border-box; margin: 0; padding: 0; }
  html, body { width: 1040px; height: 1200px; overflow: hidden; background: var(--backdrop); }
  .letterhead {
    position: absolute; left: 64px; top: 13px;
    width: 912px; height: 1174px;
    background: var(--paper);
    font-family: "Open Sans", sans-serif;
    color: var(--ink);
    overflow: hidden;
    box-shadow: 0 2px 10px rgba(0,0,0,0.15);
  }
  .brand {
    position: absolute; top: 41px; left: 0; width: 100%;
    display: flex; flex-direction: column; align-items: center; gap: 10px;
  }
  .brand-mark { width: 80px; height: 80px; border-radius: 50%; background: var(--navy); }
  .brand-name {
    font-weight: 600; font-size: 13px; letter-spacing: 0.4px;
    color: var(--navy); text-transform: uppercase;
  }
  .letter { position: absolute; left: 87px; width: 737px; font-size: 14px; line-height: 18px; }
  .issue-date { top: 212px; }
  .recipient { top: 246px; line-height: 17.7px; }
  .salutation { top: 349px; }
  .body { top: 397px; }
  .body p { line-height: 26.2px; text-align: justify; margin-bottom: 26.2px; }
  .sign-off { position: absolute; left: 87px; top: 796px; font-size: 14px; line-height: 18px; }
  .signature {
    position: absolute; left: 87px; top: 834px;
    width: 210px; height: 22px; background: #ececec; border-radius: 3px;
  }
  .signatory { position: absolute; left: 87px; top: 871px; }
  .signatory .name { font-size: 17px; line-height: 22px; font-weight: 600; color: #333; }
  .signatory .role { font-size: 14px; line-height: 18px; margin-top: 6px; }

  .footer { font-family: "Lato", sans-serif; color: var(--navy); }
  .contacts { position: absolute; left: 69px; top: 1072px; font-size: 17px; line-height: 24px; }
  .contacts .row { display: flex; align-items: center; gap: 14px; }
  .contacts .item { display: flex; align-items: center; gap: 3px; }
  .contacts svg { width: 17px; height: 17px; flex: none; }
  .divider { position: absolute; left: 472px; top: 1074px; width: 2px; height: 84px; background: var(--navy); }
  .hours { position: absolute; left: 492px; top: 1071px; font-size: 16px; line-height: 21px; }
  .hours h2 { font-size: 20px; font-weight: 700; line-height: 26px; }
  .hours b { font-weight: 700; }
  .hours-art {
    position: absolute; left: 767px; top: 1027px; width: 145px; height: 131px;
    background: var(--navy); border-radius: 70px 0 0 40px;
  }
  .base-band { position: absolute; left: 0; bottom: 0; width: 100%; height: 16px; background: var(--navy); }
</style>
</head>
<body>
<main class="letterhead">
  <header class="brand">
    <div class="brand-mark"></div>
    <div class="brand-name">Ridgeview Veterinary Surgery</div>
  </header>

  <div class="letter issue-date">Issuing Date: May 5, 2018</div>
  <div class="letter recipient">Name Of Employee Mr. XYZABC<br>Address of Employee<br>Address Line 2 etc..</div>
  <div class="letter salutation">Dear Mr.XYZABC</div>

  <section class="letter body">
    <p>Lorem Ipsum has been the industry's standard dummy text ever since the 1500s, when an unknown printer took a galley of type and scrambled it to make a type specimen book. It has survived not only five centuries, but also the leap into electronic typesetting, remaining essentially unchanged. It was popularised in the 1960s with the release of Typeline sheets containing Lorem Ipsum passages, and more recently with desktop publishing software like Pageform Studio including versions of Lorem Ipsum.</p>
    <p>Lorem Ipsum is simply dummy text of the printing and typesetting industry. Lorem Ipsum has been the industry's standard dummy text ever since the 1500s, when an unknown printer took a galley of type and scrambled it to make a type specimen book.</p>
    <p>It has survived not only five centuries, but also the leap into electronic typesetting, remaining essentially unchanged. It was popularised in the 1960s with the release of Typeline sheets containing Lorem IpsumIpsum passages.</p>
  </section>

  <div class="sign-off">Yours Sincerely</div>
  <div class="signature" role="img" aria-label="Handwritten signature of Daniel Morrow"></div>
  <div class="signatory">
    <div class="name">Daniel Morrow</div>
    <div class="role">Managing Director</div>
  </div>

  <footer class="footer">
    <div class="contacts">
      <div class="row"><span class="item">
        <svg viewBox="0 0 20 20"><circle cx="10" cy="10" r="10" fill="#0d2a52"/><path d="M10 4a4 4 0 0 0-4 4c0 3 4 8 4 8s4-5 4-8a4 4 0 0 0-4-4zm0 5.5a1.5 1.5 0 1 1 0-3 1.5 1.5 0 0 1 0 3z" fill="#fff"/></svg>
        48 Tulloch Road, Kelvale, Westmoor, 4902</span></div>
      <div class="row">
        <span class="item"><svg viewBox="0 0 20 20"><circle cx="10" cy="10" r="10" fill="#0d2a52"/><path d="M7 5l2 2.5-1 1.3c.7 1.4 1.8 2.5 3.2 3.2l1.3-1L15 13l-1.2 1.6C10 14.5 5.5 10 5.4 6.2z" fill="#fff"/></svg>07 4158 6734</span>
        <span class="item"><svg viewBox="0 0 20 20"><circle cx="10" cy="10" r="10" fill="#0d2a52"/><rect x="5" y="6.5" width="10" height="7" fill="#fff"/><path d="M5 6.5l5 4 5-4" stroke="#0d2a52" fill="none"/></svg>admin@ridgeviewvets.com.au</span>
      </div>
      <div class="row"><span class="item">
        <svg viewBox="0 0 20 20"><circle cx="10" cy="10" r="10" fill="#0d2a52"/><circle cx="10" cy="10" r="5" fill="none" stroke="#fff" stroke-width="1.4"/><path d="M5 10h10M10 5c-2 3-2 7 0 10M10 5c2 3 2 7 0 10" stroke="#fff" fill="none" stroke-width="1"/></svg>
        www.ridgeviewvets.com.au</span></div>
    </div>
    <div class="divider"></div>
    <div class="hours">
      <h2>Opening Hours</h2>
      <div><b>Monday - Friday</b> : 8am to 5pm</div>
      <div><b>Saturday:</b>&nbsp; 8am to 12pm</div>
    </div>
    <div class="hours-art" role="img" aria-label="Navy animal silhouette decoration"></div>
    <div class="base-band"></div>
  </footer>
</main>
</body>
</html>
```